Flyer-Design für Abschleppunternehmen
Zielgruppe
Wir sind ein Abschleppunternehmen und sind bestrebt neue Kunden zu gewinnen. Vor allem im Bereich 'Falschparker' suchen wir Firmen/Unternehmen mit Privatparkplätzen, die von fremden Personen zu geparkt werden. Hierzu ist stark darauf hinzuweisen, dass diese Leistung für den Autraggeber völlig kostenlos und ohne Aufwand anzufordern ist.
Aufgabenstellung
Vorschlag DIN Fyler 21x9,8cm . Wir sind ein 24/7 Betrieb. Rufnr. 073845190. Es ist darauf hinzweisen, dass wir ein unternehmen aus der direkten umgebung sind.

```html
<!DOCTYPE html>
<html lang="de">
<head>
<meta charset="utf-8">
<title>Krunzel Abschleppdienst – Flyer</title>
<link rel="stylesheet" href="https://fonts.googleapis.com/css2?family=Montserrat:wght@600;700;800&family=Open+Sans:wght@400;600&display=swap">
<style>
  :root{
    --yellow:#f0c20c;
    --red:#d2171b;
    --dark:#2a2a2a;
    --white:#ffffff;
    --ink:#1b1b1b;
    --stage:#d7d7d7;
  }
  *{box-sizing:border-box;margin:0;padding:0}
  html,body{width:1200px;height:800px;overflow:hidden}
  body{background:var(--stage);font-family:"Open Sans",sans-serif;position:relative}
  .flyer{position:absolute;top:36px;width:340px;height:728px;background:var(--yellow);overflow:hidden;box-shadow:0 6px 18px rgba(0,0,0,.18)}
  .flyer--front{left:200px}
  .flyer--back{left:660px}
  .abs{position:absolute}

  /* front */
  .service-pill{top:20px;right:0;width:150px;height:36px;background:var(--red);border-radius:18px 0 0 18px;color:var(--white);font:700 17px "Montserrat",sans-serif;display:flex;align-items:center;justify-content:center}
  .brand{top:88px;left:24px;display:flex;align-items:center;gap:8px;font:800 26px "Montserrat",sans-serif;color:var(--ink)}
  .brand__mark{width:16px;height:16px;background:var(--red)}
  .no-parking{top:58px;right:26px;width:116px;height:116px}
  .front-band{top:178px;left:0;right:0;height:320px;background:var(--dark)}
  .photo{background:linear-gradient(160deg,#a9b4c2 0%,#8a7a55 35%,#c8a21a 60%,#3b3b3b 100%)}
  .front-photo{top:190px;left:10px;right:10px;height:214px}
  .headline{top:416px;left:22px;right:16px;font-family:"Montserrat",sans-serif}
  .headline__question{color:var(--yellow);font-weight:800;font-size:30px;line-height:1.1}
  .headline__answer{color:var(--white);font-weight:800;font-size:23px;line-height:1.3}
  .pitch{top:516px;left:22px;right:18px;font-size:15px;line-height:1.45;color:var(--ink)}
  .jubilee{top:600px;left:26px;width:96px;height:96px}
  .region{top:594px;left:140px;right:14px;text-align:center;font:800 16px/1.35 "Montserrat",sans-serif;color:var(--ink)}
  .phone-row{top:668px;left:132px;right:0;display:flex;align-items:center;gap:8px}
  .phone-row__line{flex:1;height:2px;background:var(--ink)}
  .phone-row__text{font:800 17px "Montserrat",sans-serif;color:var(--ink)}
  .phone-row__tail{width:24px;height:2px;background:var(--ink)}
  .footer-rule{bottom:14px;left:16px;right:16px;height:2px;background:var(--ink)}

  /* back */
  .back-photo{top:0;left:0;right:0;height:160px;background:linear-gradient(170deg,#dfe4ea 0%,#8e98a4 40%,#d9b51e 70%,#55585c 100%)}
  .ribbon{top:150px;left:0;width:300px;height:42px;background:var(--dark);clip-path:polygon(0 0,92% 0,100% 100%,0 100%);color:var(--white);font:800 17px "Montserrat",sans-serif;display:flex;align-items:center;padding-left:18px}
  .services{top:208px;left:20px;list-style:none;font-size:15.5px;line-height:1.62;color:var(--ink)}
  .services li::before{content:"• "}
  .badge-247{top:266px;right:0;width:100px;height:104px;background:var(--red)}
  .gallery{top:400px;left:0;right:0;height:328px;background:var(--dark)}
  .gallery__grid{position:absolute;top:10px;left:10px;right:10px;height:250px;display:grid;grid-template-columns:1fr 1fr;grid-template-rows:1fr 1fr;gap:6px}
  .gallery__tile{background:linear-gradient(150deg,#7b8896 0%,#8c6a3e 40%,#e0bb12 65%,#4a4a4a 100%)}
  .gallery__tile--garage{background:linear-gradient(150deg,#9a9ea4 0%,#6d7075 40%,#e2bd14 65%,#b9bcc0 100%)}
  .website{bottom:20px;left:0;right:0;text-align:center;color:var(--white);font:700 17px "Montserrat",sans-serif}
</style>
</head>
<body>

<section class="flyer flyer--front">
  <div class="abs service-pill">24/7 Service</div>
  <div class="abs brand"><span class="brand__mark"></span>Krunzel</div>

  <svg class="abs no-parking" viewBox="0 0 116 116" aria-label="Parkverbot-Schild">
    <circle cx="58" cy="58" r="56" fill="#fff"/>
    <circle cx="58" cy="58" r="44" fill="#fff" stroke="#d2171b" stroke-width="9"/>
    <text x="58" y="82" text-anchor="middle" font-family="Montserrat,sans-serif" font-weight="800" font-size="64" fill="#1b1b1b">P</text>
    <line x1="80" y1="26" x2="36" y2="90" stroke="#d2171b" stroke-width="8"/>
  </svg>

  <div class="abs front-band"></div>
  <div class="abs photo front-photo" role="img" aria-label="Foto: gelber Abschlepp-LKW mit Kran vor herbstlichen Bäumen"></div>
  <div class="abs headline">
    <div class="headline__question">Falschparker?</div>
    <div class="headline__answer">Wir erledigen für sie!</div>
  </div>

  <p class="abs pitch">Lassen sie unberechtigt geparkte fahrzeuge kostenlos abschleppen!<br>Ein Anruf genügt</p>

  <svg class="abs jubilee" viewBox="0 0 96 96" aria-label="50 Jahre">
    <polygon fill="#c4161b" points="48,0 55,8 65,3 68,13 79,12 78,23 88,26 84,36 94,42 87,50 94,58 85,63 89,73 78,75 79,86 68,85 64,95 55,89 48,96 41,89 32,95 28,85 17,86 18,75 7,73 11,63 2,58 9,50 2,42 12,36 8,26 18,23 17,12 28,13 31,3 41,8"/>
    <text x="46" y="52" text-anchor="middle" font-family="Montserrat,sans-serif" font-weight="800" font-size="32" fill="#fff">50</text>
    <text x="50" y="72" text-anchor="middle" font-family="Open Sans,sans-serif" font-weight="600" font-size="16" fill="#fff">Jahre</text>
  </svg>

  <p class="abs region">Wir sind ihr<br>Abschleppdienst<br>der Region!</p>

  <div class="abs phone-row">
    <span class="phone-row__line"></span>
    <span class="phone-row__text">Tel. 07384 5190</span>
    <span class="phone-row__tail"></span>
  </div>
  <div class="abs footer-rule"></div>
</section>

<section class="flyer flyer--back">
  <div class="abs back-photo" role="img" aria-label="Foto: Abschleppwagen mit gelbem Sportwagen auf der Ladefläche"></div>
  <div class="abs ribbon">Wir können auch mehr!</div>

  <ul class="abs services">
    <li>PKW Abschlepp-Bergungsdienst</li>
    <li>LKW Abschlepp-Bergungsdienst</li>
    <li>Kranservice</li>
    <li>Fahrzeugtransporte</li>
    <li>Ölspurbesitigung</li>
    <li>Fahrzeugöffnungen</li>
  </ul>

  <svg class="abs badge-247" viewBox="0 0 100 104" aria-label="24/7 Service">
    <rect width="100" height="104" fill="#d2171b"/>
    <path d="M72 28 A30 30 0 1 0 80 52" fill="none" stroke="#fff" stroke-width="3.5"/>
    <path d="M62 22 L74 27 L70 39" fill="none" stroke="#fff" stroke-width="3.5"/>
    <text x="50" y="58" text-anchor="middle" font-family="Montserrat,sans-serif" font-weight="800" font-size="20" fill="#fff">24/7</text>
    <text x="50" y="72" text-anchor="middle" font-family="Montserrat,sans-serif" font-weight="700" font-size="9" fill="#fff">SERVICE</text>
  </svg>

  <div class="abs gallery">
    <div class="gallery__grid">
      <div class="gallery__tile" role="img" aria-label="Foto: gelbes Pannenhilfe-Fahrzeug vor Bäumen"></div>
      <div class="gallery__tile" role="img" aria-label="Foto: gelbes Pannenhilfe-Fahrzeug in der Abenddämmerung"></div>
      <div class="gallery__tile gallery__tile--garage" role="img" aria-label="Foto: gelber Pick-up in einer Tiefgarage"></div>
      <div class="gallery__tile gallery__tile--garage" role="img" aria-label="Foto: Pannenhilfe-Fahrzeug im Parkhaus"></div>
    </div>
    <div class="abs website">www.autohilfe-krunzel.de</div>
  </div>
</section>

</body>
</html>
```